Hack my website! Blue Harbor needs a site

We hack stuff. No joke, that is what we do, but we are the good guys!

We do security consulting, specifically offensive security. The technical term is "Penetration Testing", but you probably know it as "hacking". Companies hire us to break in before the bad guys do. (I have a very cool job :) ).

I need a web site to describe our offerings and connect with clients.

I've included my business card and logo so you can understand what I'm looking for on the website and the color scheme.

Tag line:
Offensive Services from Offensive Minds

Target Market(s)

Medium to large businesses

Industry/Entity Type

Computer Security

Coding

Coded - Design and coding required

Number of Pages Required

2 page

Font styles to use
Sans Serif

Colors

Designer to choose colors to be used in the design.

Requirements
Must have
• Flat, clean, professional look
Nice to have
• Bonus for bootstrap. See the uploaded logo for the current colors. I'd really like this to look decent on a phone too.
Should not have
• 1. Black background
• 2. The business card is to show the colors and theme so far. Please, do NOT just slam that into the middle of the site since it doesn't make sense. It feels odd that I have to say that, but I've received multiple submissions where people have done this.

```html
<!DOCTYPE html>
<html lang="en">
<head>
<meta charset="utf-8">
<title>Blue Harbor — Information Security</title>
<link href="https://fonts.googleapis.com/css2?family=Oswald:wght@300;400;500&family=Roboto:wght@400;500;700&family=Ubuntu:wght@400;500&display=swap" rel="stylesheet">
<style>
:root{
  --red:#d0202a;
  --red-dark:#b81b24;
  --navy:#0c1f3c;
  --blue:#1f5d9a;
  --ink:#2a2a2a;
  --grey:#666;
  --paper:#ffffff;
  --footer:#2f2f2f;
}
*{margin:0;padding:0;box-sizing:border-box}
html,body{width:1200px;height:2655px;overflow:hidden;background:var(--paper)}
body{position:relative;font-family:'Roboto',sans-serif;color:var(--ink)}
.abs{position:absolute}

/* hero */
.hero{left:0;top:0;width:1200px;height:559px;background:radial-gradient(ellipse at 55% 45%,#2a5b95 0%,#143460 40%,#081a33 80%,#050f20 100%)}
.brand-box{left:0;top:14px;width:370px;height:57px;background:#e9e9e9;display:flex;align-items:center;justify-content:center;gap:12px}
.brand-mark{width:20px;height:20px;background:var(--red)}
.brand-name{font-family:'Roboto',sans-serif;font-weight:500;font-size:24px;letter-spacing:4px;color:var(--red);text-transform:uppercase}
.nav{left:370px;top:28px;width:667px;height:32px;background:var(--red);display:flex;justify-content:space-around;align-items:center}
.nav a{color:#fff;font-size:14px;text-decoration:none;text-transform:uppercase}
.hero-kicker{left:161px;top:205px;font-family:'Oswald',sans-serif;font-weight:300;font-size:42px;color:#fff;letter-spacing:-.5px;line-height:52px}
.hero-title{left:158px;top:256px;font-family:'Oswald',sans-serif;font-weight:500;font-size:66px;color:#fff;line-height:1}
.hero-text{left:161px;top:340px;width:450px;font-size:11px;line-height:16px;color:#e6e9ef}
.hero-btn{left:161px;top:395px;width:136px;height:39px;border:2px solid #fff;border-radius:20px;background:var(--red);color:#fff;font-size:15px;display:flex;align-items:center;justify-content:center;gap:6px;text-transform:uppercase}
.arrow{top:262px;width:32px;height:32px}
.tiles{left:874px;top:223px;width:163px;height:163px;display:grid;grid-template-columns:1fr 1fr;gap:3px}
.tile{display:flex;align-items:center;justify-content:center}
.tile.blue{background:#2a6fb5}.tile.red{background:#b81b24}

/* logo band */
.logo-band{left:0;top:559px;width:1200px;height:156px;background:#f6f6f6;text-align:center}
.logo-band .name{position:absolute;left:0;right:0;top:44px;font-weight:700;font-size:48px;letter-spacing:10px;color:var(--red);text-transform:uppercase}
.logo-band .sub{position:absolute;left:0;right:0;top:102px;font-size:14px;letter-spacing:9px;color:#222}

/* about */
.about{left:0;top:715px;width:641px;height:296px;background:var(--red);color:#fff}
.about-body{position:absolute;left:161px;top:38px;width:462px}
.about h2{font-weight:400;font-size:36px;line-height:40px;letter-spacing:1px;text-transform:uppercase}
.about .tag{font-size:16px;line-height:20px;letter-spacing:1px;margin-bottom:10px}
.about p{font-size:10px;line-height:15px;margin-bottom:9px}
.about-photo{left:641px;top:715px;width:559px;height:296px;background:linear-gradient(135deg,#f2f2f2 0%,#cfcfcf 45%,#9a9a9a 75%,#e8e8e8 100%)}

/* services */
.services{left:0;top:1011px;width:1200px;height:538px;background:linear-gradient(180deg,#f4f4f4,#ececec)}
.sec-mark{width:26px;height:30px;background:var(--red)}
.sec-title{left:0;right:0;text-align:center;font-family:'Ubuntu',sans-serif;font-weight:500;font-size:40px;color:#333;letter-spacing:-1px}
.sec-title b{color:var(--red);font-weight:500}
.sec-rule{left:580px;width:40px;height:3px;background:var(--red)}
.svc{width:450px;height:120px}
.svc .ring{position:absolute;left:0;top:0;width:98px;height:98px;border-radius:50%;border:3px solid var(--red);background:#fff;display:flex;align-items:center;justify-content:center}
.svc .ring::before{content:"";position:absolute;inset:4px;border-radius:50%;border:1px solid #e8a0a4}
.svc-body{position:absolute;left:114px;top:0;width:275px;display:flex;flex-direction:column}
.svc h3{font-family:'Ubuntu',sans-serif;font-weight:500;font-size:18px;line-height:24px;text-transform:uppercase;color:#222;margin-bottom:4px}
.svc p{font-size:9px;line-height:13px;color:#555}
.svc .more{font-size:9.5px;line-height:13px;color:var(--red);margin-top:5px}

/* stats */
.stats{left:0;top:1549px;width:1200px;height:120px;background:var(--red-dark)}
.stat{top:18px;width:250px;text-align:center;color:#fff}
.stat .num{font-family:'Oswald',sans-serif;font-weight:400;font-size:48px;line-height:60px}
.stat .lbl{font-family:'Oswald',sans-serif;font-weight:300;font-size:15px;letter-spacing:.5px;text-transform:uppercase}

/* testimonials */
.avatar{left:550px;top:1877px;width:100px;height:100px;border-radius:50%;background:radial-gradient(circle at 50% 40%,#f1dcd2,#c9b5aa);border:3px solid #fff;box-shadow:0 0 0 1px #ddd}
.quote-text{left:352px;top:2018px;width:540px;font-size:16px;line-height:23px;color:#666}
.client-name{left:352px;top:2141px;font-size:16px;color:var(--red);text-transform:uppercase}
.client-role{left:352px;top:2162px;font-size:13px;color:#333}
.dots{left:352px;top:2199px;display:flex;gap:8px}
.dots span{width:12px;height:12px;border-radius:50%;border:1px solid #999}
.dots span.on{background:var(--red);border-color:var(--red)}

/* footer */
.footer{left:0;top:2294px;width:1200px;height:317px;background:linear-gradient(160deg,#3a3a3a,#262626)}
.f-head{font-size:19px;font-weight:400;color:#fff;text-transform:uppercase;letter-spacing:.5px}
.post{width:290px;font-size:10.5px;line-height:15px;color:#fff}
.post .more{color:var(--red);font-size:10px}
.links{list-style:none}
.links li{font-size:12px;color:#fff;line-height:27px}
.links li::before{content:"›";color:var(--red);margin-right:6px}
.nl-input{left:841px;top:2372px;width:198px;height:41px;background:#d9d9d9;font-size:11px;color:#666;padding:14px 14px}
.nl-btn{left:841px;top:2428px;width:95px;height:29px;background:var(--red);border:1px solid #fff;color:#fff;font-size:12px;font-weight:700;display:flex;align-items:center;justify-content:center;text-transform:uppercase}
.social{top:2571px;width:27px;height:27px;border-radius:50%;background:#5a6270}
.copyright{left:0;top:2611px;width:1200px;height:44px;background:var(--red);color:#fff;font-size:11px;display:flex;align-items:center;justify-content:center}
</style>
</head>
<body>

<section class="abs hero" role="img" aria-label="Dark blue technology backdrop with padlock, laptops and circular arrows"></section>
<div class="abs brand-box"><span class="brand-mark"></span><span class="brand-name">Blue Harbor</span></div>
<nav class="abs nav"><a>Home</a><a>About</a><a>What we do</a><a>Services</a><a>Contact</a><a>Search</a></nav>

<svg class="abs arrow" style="left:12px" viewBox="0 0 32 32"><circle cx="16" cy="16" r="15" fill="#9aa3ad"/><path d="M19 8 11 16l8 8" fill="none" stroke="#1b2b44" stroke-width="4"/></svg>
<svg class="abs arrow" style="left:1145px" viewBox="0 0 32 32"><circle cx="16" cy="16" r="15" fill="#9aa3ad"/><path d="M13 8l8 8-8 8" fill="none" stroke="#1b2b44" stroke-width="4"/></svg>

<div class="abs hero-kicker">Offensive Solutions from</div>
<h1 class="abs hero-title">OFFENSIVE MINDS</h1>
<p class="abs hero-text">Lorem Ipsum is simply dummy text of the printing and typesetting industry. Lorem Ipsum has been the industry's standard dummy text ever since the 1500s...</p>
<div class="abs hero-btn"><svg width="16" height="14" viewBox="0 0 16 14"><path d="M9 1l6 5-6 5V8C5 8 2 9 1 13 1 7 4 4 9 4z" fill="#fff"/></svg>Get Started</div>

<div class="abs tiles">
  <div class="tile blue"><svg width="52" height="44" viewBox="0 0 52 44" fill="none" stroke="#fff" stroke-width="2"><rect x="2" y="2" width="48" height="32"/><path d="M18 42h16M26 34v8M10 12h14M10 18h20M10 24h10"/><circle cx="38" cy="18" r="6"/></svg></div>
  <div class="tile red"><svg width="44" height="48" viewBox="0 0 44 48" fill="none" stroke="#fff" stroke-width="2"><rect x="4" y="6" width="28" height="38"/><rect x="12" y="2" width="12" height="6"/><circle cx="18" cy="22" r="5"/><path d="M10 36c2-6 14-6 16 0"/><circle cx="34" cy="36" r="7"/><path d="M30 36l3 3 5-5"/></svg></div>
  <div class="tile red"><svg width="40" height="48" viewBox="0 0 40 48" fill="none" stroke="#fff" stroke-width="2"><path d="M10 20v-8a10 10 0 0 1 20 0v8"/><rect x="4" y="20" width="32" height="26" rx="3"/><circle cx="20" cy="31" r="4"/><path d="M20 35v5"/></svg></div>
  <div class="tile blue"><svg width="48" height="44" viewBox="0 0 48 44" fill="none" stroke="#fff" stroke-width="2"><rect x="2" y="2" width="44" height="30"/><path d="M16 42h16M24 32v10"/><circle cx="24" cy="17" r="8"/><path d="M24 7v10"/></svg></div>
</div>

<section class="abs logo-band">
  <div class="name">Blue Harbor</div>
  <div class="sub">INFORMATION SECURITY</div>
</section>

<section class="abs about">
  <div class="about-body">
    <h2>About Blue Harbor</h2>
    <div class="tag">Offensive Solutions from Offensive Minds</div>
    <p>Lorem Ipsum is simply dummy text of the printing and typesetting industry. Lorem Ipsum has been the industry's standard dummy text ever since the 1500s, when an unknown printer took a galley of type and scrambled it to make a type specimen book. It has survived not only five centuries, but also the leap into electronic typesetting, remaining essentially unchanged. It was popularised in the 1960s with the release of Letraset sheets containing Lorem Ipsum passages, and more recently with desktop...</p>
    <p>Lorem Ipsum is simply dummy text of the printing and typesetting industry. Lorem Ipsum has been the industry's standard dummy text ever since the 1500s, when an unknown printer took a galley of type and scrambled it to make a type specimen book. It has survived not only five centuries...</p>
  </div>
</section>
<div class="abs about-photo" role="img" aria-label="Photo of a hand typing on a laptop keyboard"></div>

<section class="abs services" role="img" aria-label="Faint photo of a computer workspace behind the services"></section>
<div class="abs sec-mark" style="left:587px;top:1043px"></div>
<h2 class="abs sec-title" style="top:1100px"><b>WHAT</b> WE DO?</h2>
<div class="abs sec-rule" style="top:1160px"></div>

<div class="abs svc" style="left:162px;top:1220px">
  <div class="ring"><svg width="50" height="50" viewBox="0 0 50 50" fill="none" stroke="#1d3556" stroke-width="3"><circle cx="25" cy="10" r="6"/><circle cx="11" cy="38" r="6" fill="#1d3556"/><circle cx="39" cy="38" r="6" fill="#1d3556"/><path d="M22 16l-8 16M28 16l8 16M17 38h16"/></svg></div>
  <div class="svc-body">
    <h3>Security Consulting</h3>
    <p>Lorem Ipsum is simply dummy text of the printing and typesetting industry. Lorem Ipsum has been the industry's standard dummy text ever since the 1500s, when an unknown printer took a galley of type and scrambled it to make a type specimen book. It has survived not only five centuries...</p>
    <div class="more">Read More »</div>
  </div>
</div>
<div class="abs svc" style="left:659px;top:1220px">
  <div class="ring"><svg width="44" height="50" viewBox="0 0 44 50" fill="none" stroke="#1d3556" stroke-width="3"><path d="M22 3 4 10v14c0 12 8 20 18 24 10-4 18-12 18-24V10z"/><path d="M13 25l7 7 12-13"/></svg></div>
  <div class="svc-body">
    <h3>Offensive Security</h3>
    <p>Lorem Ipsum is simply dummy text of the printing and typesetting industry. Lorem Ipsum has been the industry's standard dummy text ever since the 1500s, when an unknown printer took a galley of type and scrambled it to make a type specimen book. It has survived not only five centuries...</p>
    <div class="more">Read More »</div>
  </div>
</div>
<div class="abs svc" style="left:162px;top:1378px">
  <div class="ring"><svg width="50" height="50" viewBox="0 0 50 50" fill="none" stroke="#1d3556" stroke-width="2.5"><path d="M8 25a17 17 0 0 1 30-11M42 25a17 17 0 0 1-30 11"/><path d="M38 6v8h-8M12 44v-8h8"/><path d="M19 24v-4a6 6 0 0 1 12 0v4"/><rect x="16" y="24" width="18" height="13" rx="2"/></svg></div>
  <div class="svc-body">
    <h3>Penetration Testing</h3>
    <p>Lorem Ipsum is simply dummy text of the printing and typesetting industry. Lorem Ipsum has been the industry's standard dummy text ever since the 1500s, when an unknown printer took a galley of type and scrambled it to make a type specimen book. It has survived not only five centuries...</p>
    <div class="more">Read More »</div>
  </div>
</div>
<div class="abs svc" style="left:659px;top:1378px">
  <div class="ring"><svg width="50" height="46" viewBox="0 0 50 46" fill="none" stroke="#1d3556" stroke-width="3"><rect x="3" y="3" width="44" height="30"/><path d="M17 43h16M25 33v10"/><path d="M12 14l8 5 10-5 8 0M14 14h8M28 14h8" /></svg></div>
  <div class="svc-body">
    <h3>Break Hacking</h3>
    <p>Lorem Ipsum is simply dummy text of the printing and typesetting industry. Lorem Ipsum has been the industry's standard dummy text ever since the 1500s, when an unknown printer took a galley of type and scrambled it to make a type specimen book. It has survived not only five centuries...</p>
    <div class="more">Read More »</div>
  </div>
</div>

<section class="abs stats">
  <div class="abs stat" style="left:105px"><div class="num">100%</div><div class="lbl">Offensive Security</div></div>
  <div class="abs stat" style="left:355px"><div class="num">980</div><div class="lbl">Happy Client</div></div>
  <div class="abs stat" style="left:610px"><div class="num">100%</div><div class="lbl">Security Guarantee</div></div>
  <div class="abs stat" style="left:870px"><div class="num">630</div><div class="lbl">Comments</div></div>
</section>

<div class="abs sec-mark" style="left:587px;top:1726px"></div>
<h2 class="abs sec-title" style="top:1774px"><b>CLIENT</b> TESTIMONIALS</h2>
<div class="abs sec-rule" style="top:1831px"></div>

<div class="abs avatar" role="img" aria-label="Portrait photo of the client"></div>
<svg class="abs" style="left:225px;top:1995px" width="110" height="68" viewBox="0 0 110 68" fill="none" stroke="#c8ccdc" stroke-width="3"><path d="M28 66C10 56 2 42 2 28a25 25 0 1 1 40 20"/><path d="M84 66C66 56 58 42 58 28a25 25 0 1 1 40 20"/></svg>
<p class="abs quote-text">Lorem Ipsum is simply dummy text of the printing and typesetting industry. Lorem Ipsum has been the industry's standard dummy text ever since the 1500s, when an unknown printer took a galley of type and scrambled it to make a type specimen book.</p>
<div class="abs client-name">Mara Lindqvist</div>
<div class="abs client-role">Happy client</div>
<div class="abs dots"><span class="on"></span><span></span><span></span></div>
<svg class="abs" style="left:867px;top:2155px" width="110" height="66" viewBox="0 0 110 66" fill="none" stroke="#c8ccdc" stroke-width="3"><path d="M26 2C44 12 52 26 52 40a25 25 0 1 1-40-20"/><path d="M82 2c18 10 26 24 26 38a25 25 0 1 1-40-20"/></svg>

<footer class="abs footer" role="img" aria-label="Dark street map backdrop of the office area"></footer>
<h4 class="abs f-head" style="left:161px;top:2328px">Recent Posts</h4>
<div class="abs post" style="left:161px;top:2365px">Lorem Ipsum is simply dummy text of the printing and typesetting industry...<br><span class="more">Read More »</span></div>
<div class="abs post" style="left:161px;top:2428px">Lorem Ipsum is simply dummy text of the printing and typesetting industry...<br><span class="more">Read More »</span></div>
<div class="abs post" style="left:161px;top:2489px">Lorem Ipsum is simply dummy text of the printing and typesetting industry...<br><span class="more">Read More »</span></div>
<div class="abs social" style="left:161px"></div>
<div class="abs social" style="left:198px"></div>
<div class="abs social" style="left:236px"></div>
<div class="abs social" style="left:271px"></div>

<h4 class="abs f-head" style="left:566px;top:2328px">Quick Link</h4>
<ul class="abs links" style="left:572px;top:2359px"><li>Home</li><li>About</li><li>What we do?</li><li>Services</li><li>Search</li><li>Contact Us</li></ul>

<h4 class="abs f-head" style="left:841px;top:2328px">Newsletter</h4>
<div class="abs nl-input">Enter Your Email Id</div>
<div class="abs nl-btn">Subscribe</div>

<div class="abs copyright">Copyright 2017. All Right Reserved.</div>

</body>
</html>
```